2024 Ridgeway Financial Team Deck

I have created a power point slide deck and I need the slide deck recreated. Organized, with better color, background pictures, etc. I am thinking the colors for the presentation can be navy blue, and white, and gold, with hints of silver and black. We are financial planning firm that specializes in working with tech companies in silicon valley.

```html
<!DOCTYPE html>
<html lang="en">
<head>
<meta charset="utf-8">
<title>Ridgeway Financial 2024 Team Deck</title>
<link href="https://fonts.googleapis.com/css2?family=Roboto:wght@300;400;500;700&family=Roboto+Condensed:wght@700&display=swap" rel="stylesheet">
<style>
:root{
  --canvas:#f8f2e2;
  --navy:#0f0f4f;
  --navy-deep:#06062e;
  --gold:#fdbd08;
  --ink:#2b2b2b;
  --text:#4a4a4a;
  --silver:#e9e9ec;
  --white:#ffffff;
}
*{box-sizing:border-box;margin:0;padding:0}
html,body{width:1200px;height:4051px;overflow:hidden}
body{background:var(--canvas);font-family:"Roboto",sans-serif;color:var(--text);position:relative}
.slide{position:absolute;left:77px;width:1046px;height:588px;overflow:hidden;
  background:linear-gradient(135deg,#fbfbfb 0%,#ededed 35%,#f8f8f8 60%,#e9e9e9 100%);
  box-shadow:0 3px 10px rgba(0,0,0,.12)}
.abs{position:absolute}
.title{position:absolute;left:0;right:0;top:36px;text-align:center;font-family:"Roboto Condensed",sans-serif;font-weight:700;font-size:35px;color:var(--ink);letter-spacing:.5px}
.title::after{content:"";display:block;width:50px;height:3px;background:var(--gold);margin:2px auto 0}
.footer-line{position:absolute;left:0;right:0;top:556px;height:2px;background:var(--navy)}
.page-no{position:absolute;left:946px;top:542px;width:30px;height:30px;background:var(--navy);transform:rotate(45deg)}
.page-no span{display:block;transform:rotate(-45deg);color:#fff;font-size:11px;font-weight:500;text-align:center;line-height:30px}
.bullets{list-style:none}
.bullets li{position:relative;padding-left:22px}
.bullets li::before{content:"";position:absolute;left:0;top:.35em;width:8px;height:8px;border:2px solid var(--gold);border-radius:50%}
.photo{position:absolute}
/* cover */
.cover .photo{left:0;top:0;width:717px;height:588px;background:linear-gradient(120deg,#d9dde4 0%,#eef1f5 45%,#f7f8fa 100%)}
.cover-title{position:absolute;left:706px;top:176px;font-weight:300;font-size:56px;line-height:81px;color:#d6d6dc}
/* mission */
.subtitle{position:absolute;left:150px;right:150px;top:108px;text-align:center;font-size:18px;line-height:27px;color:#333}
.card{position:absolute;top:217px;width:392px;height:302px;background:#fff;box-shadow:0 2px 8px rgba(0,0,0,.12)}
.card-icon{position:absolute;left:157px;top:-39px;width:78px;height:78px;border-radius:50%;background:var(--gold);display:flex;align-items:center;justify-content:center}
.card h3{margin-top:68px;text-align:center;font-size:12px;font-weight:700;color:#111}
.card .bullets{margin:16px 24px 0 24px;font-size:10px;line-height:16px;color:#444}
.card .bullets li{margin-bottom:8px}
/* vision */
.vision-text{position:absolute;left:510px;top:110px;width:478px;font-size:9.6px;line-height:15.6px;color:#444}
.vision-text li{margin-bottom:3px}
/* bonus */
.bonus-icon{position:absolute;width:78px;height:78px;border-radius:50%;background:var(--navy-deep);display:flex;align-items:center;justify-content:center}
.bonus-head{position:absolute;left:250px;font-size:14px;font-weight:700;color:#111}
.bonus-list{position:absolute;left:250px;font-size:12px;line-height:24px;color:#555}
/* recap */
.frame{position:absolute;top:121px;width:241px;height:238px;border:1.5px solid var(--navy)}
.frame.dashed{border-style:dashed}
.tile{position:absolute;left:19px;top:19px;width:201px;height:198px;display:flex;flex-direction:column;align-items:center;justify-content:center;color:#fff;font-size:14px;font-weight:700;box-shadow:0 0 0 5px #fff}
.tile svg{margin-bottom:22px}
.recap-list{position:absolute;top:382px;font-size:9.5px;line-height:18px;color:#555}
.recap-list li{padding-left:18px}
.recap-list li::before{width:7px;height:7px;top:5px}
/* aum */
.aum-icon{position:absolute;width:70px;height:70px;border-radius:50%;background:var(--navy-deep);display:flex;align-items:center;justify-content:center}
.aum-label{position:absolute;font-size:12px;font-weight:700;color:#222;line-height:20px}
</style>
</head>
<body>

<!-- Slide 1: cover -->
<section class="slide cover" style="top:88px">
  <div class="photo" role="img" aria-label="Photo of two advisors in business attire reviewing a tablet at a bright office desk"></div>
  <svg class="abs" style="left:0;top:0" width="1046" height="588" viewBox="0 0 1046 588">
    <polygon points="332,0 1046,0 1046,588 717,588" fill="#06062e"/>
    <polygon points="320,0 332,0 717,588 700,588" fill="#14145a"/>
    <polygon points="348,0 717,0 525,277" fill="#fdbd08"/>
  </svg>
  <h1 class="cover-title">RIDGEWAY<br>FINANCIAL<br>2024</h1>
</section>

<!-- Slide 2: mission -->
<section class="slide" style="top:745px">
  <h2 class="title">MISSION STATEMENT</h2>
  <p class="subtitle">To provide our client with the systems and processes needed to Guide their Hero’s journey and leave an Impact</p>
  <article class="card" style="left:116px">
    <div class="card-icon">
      <svg width="40" height="40" viewBox="0 0 40 40" fill="none" stroke="#1a1a1a" stroke-width="1.6"><rect x="6" y="8" width="18" height="26"/><line x1="10" y1="14" x2="20" y2="14"/><line x1="10" y1="19" x2="20" y2="19"/><line x1="10" y1="24" x2="20" y2="24"/><rect x="22" y="18" width="12" height="16"/><circle cx="30" cy="9" r="5"/></svg>
    </div>
    <h3>THE HERO’S JOURNEY</h3>
    <ul class="bullets">
      <li>We believe everyone has a purpose, God’s purpose in their life, and it is our mission to help our clients relentlessly pursue their purpose. A life with purpose is a life living out your Hero’s Journey!</li>
    </ul>
  </article>
  <article class="card" style="left:536px">
    <div class="card-icon">
      <svg width="40" height="40" viewBox="0 0 40 40" fill="none" stroke="#1a1a1a" stroke-width="1.6"><rect x="5" y="7" width="30" height="21"/><line x1="20" y1="28" x2="20" y2="34"/><line x1="13" y1="34" x2="27" y2="34"/><polyline points="9,23 15,17 20,20 27,12"/></svg>
    </div>
    <h3>HOW</h3>
    <ul class="bullets">
      <li>Our financial planning &amp; wealth management services give our clients</li>
      <li>More Time &amp; Clarity on their plan and what is needed to accomplish the objective</li>
      <li>We help our clients think bigger and professionally hold them accountable to their goals</li>
      <li>We help reduce taxes drag, increase diversification, reduce investment risk, &amp; maximize investment returns so that our clients have the financial resources to maximize their potential and ultimately leave a larger Impact on the world.</li>
    </ul>
  </article>
  <div class="footer-line"></div><div class="page-no"><span>2</span></div>
</section>

<!-- Slide 3: vision -->
<section class="slide" style="top:1403px">
  <h2 class="title">FIRM VISION (DECEMBER 2026)</h2>
  <div class="photo" style="left:60px;top:134px;width:409px;height:325px;background:linear-gradient(135deg,#eef0f3 0%,#c9ccd2 55%,#8a8f98 100%)" role="img" aria-label="Photo of a hand working a calculator over printed financial reports"></div>
  <ul class="bullets vision-text">
    <li>We are an elite wealth management firm at Harborline Mutual, that is impact driven and focused on the clients’ goals, needs, and objectives above all else. We specialize in serving Executives, Directors, &amp; Vice Presidents at Orchard Tech, Searchwell, Lumen Social, &amp; other tech companies where a heavy part of compensation is coming in the form of stock (RSU/ESPP).</li>
    <li>Over the last 3 years we have grown the firm organically, through introductions, and seminars/speaking events.</li>
    <li>We are the primary advisory firm &amp; financial planning relationship for 300 households in this space. We manage over $150m in assets and our minimize account size has grown to $500k. We are consistently qualifying for forum and this year (awards year 2026) we will have $1M premium and $1M GDC in just 8 years at Harborline Mutual.</li>
    <li>Our team has 3 lead advisors that are each fully responsible for servicing a sleeve of 80 – 125 clients on an annual basis. Each advisor is also responsible for bringing on an additional $6M of AUM annually, 10 new clients, and writing $150k of premium.</li>
    <li>Our team has a mandatory team trip every year, we don’t work weekends, we rarely work past 5pm, and we have frogman Fridays. Every Friday the team is off by 1pm at the latest, we get in, get shit done, and get out.</li>
    <li>Daniel is only taking client meetings 4 days/week and takes no more then 16 on any given week. He has a 2nd chair in every meeting that is taking notes and will be responsive for the follow up. The calendar is filled by the lead advisors who are working on a path to partnership at the firm. Everyone is financially tied to bottom line revenue. We have a team of winners!</li>
    <li>We are healthy, fit, &amp; happy. We have the opportunity to help who we want when we want. We have control over our lives and work schedule. We dictate the pace and cadence that we want to move at based on our goals any given year. Every member of the team loves the team, supports the mission, and wants to leave an impact.</li>
    <li>We are well on our way to managing $1B by December 2033</li>
  </ul>
  <div class="footer-line"></div><div class="page-no"><span>3</span></div>
</section>

<!-- Slide 4: bonus -->
<section class="slide" style="top:2060px">
  <h2 class="title">BONUS &amp; INCENTIVE</h2>
  <div class="bonus-icon" style="left:151px;top:225px">
    <svg width="42" height="42" viewBox="0 0 42 42" fill="none" stroke="#fff" stroke-width="1.6"><rect x="6" y="6" width="18" height="12" rx="2"/><rect x="18" y="12" width="18" height="12" rx="2"/><circle cx="11" cy="29" r="4"/><circle cx="31" cy="29" r="4"/><path d="M4 39c1-5 4-6 7-6s6 1 7 6M24 39c1-5 4-6 7-6s6 1 7 6"/></svg>
  </div>
  <div class="bonus-head" style="top:230px">FORUM $738K</div>
  <ul class="bullets bonus-list" style="top:258px">
    <li>Jess: Trip to Sunny Kingdom Park</li>
    <li>Marco: Cash Bonus</li>
  </ul>
  <div class="bonus-icon" style="left:151px;top:340px">
    <svg width="42" height="42" viewBox="0 0 42 42" fill="none" stroke="#fff" stroke-width="1.8"><polygon points="8,15 14,7 28,7 34,15 21,35"/><line x1="8" y1="15" x2="34" y2="15"/><polyline points="14,7 17,15 21,35 25,15 28,7"/></svg>
  </div>
  <div class="bonus-head" style="top:345px">$1M PREMIUM</div>
  <ul class="bullets bonus-list" style="top:373px">
    <li>Jess: $12k Bonus</li>
    <li>Delgado: $12k Bonus</li>
  </ul>
  <svg class="abs" style="left:495px;top:127px" width="420" height="420" viewBox="0 0 420 420">
    <path d="M48 78 A190 190 0 0 1 392 270" fill="none" stroke="#fdbd08" stroke-width="4"/>
  </svg>
  <div class="photo" style="left:542px;top:174px;width:326px;height:326px;border-radius:50%;background:radial-gradient(circle at 55% 45%,#d7d3cc 0%,#8b7a66 55%,#3c3029 100%)" role="img" aria-label="Photo of two professionals passing a tablet across a wooden desk beside a laptop and plant"></div>
  <div class="footer-line"></div><div class="page-no"><span>4</span></div>
</section>

<!-- Slide 5: recap -->
<section class="slide" style="top:2718px">
  <h2 class="title">36-MONTH RECAP</h2>
  <div class="frame dashed" style="left:116px">
    <div class="tile" style="background:#5b5b5b">
      <svg width="44" height="44" viewBox="0 0 44 44" fill="none" stroke="#fff" stroke-width="1.6"><rect x="5" y="6" width="28" height="22"/><polyline points="10,22 16,15 21,19 28,11"/><circle cx="32" cy="31" r="7"/><line x1="37" y1="36" x2="41" y2="40"/></svg>
      2021: 2ND YEAR
    </div>
  </div>
  <div class="frame dashed" style="left:403px;border-top-style:solid">
    <div class="tile" style="background:#0c0c0c">
      <svg width="44" height="44" viewBox="0 0 44 44" fill="none" stroke="#fff" stroke-width="1.6"><rect x="8" y="4" width="28" height="22"/><circle cx="22" cy="13" r="4"/><path d="M15 24c1-4 4-6 7-6s6 2 7 6"/><path d="M6 40l8-8h16l8 8"/></svg>
      2022: 3RD YEAR
    </div>
  </div>
  <div class="frame dashed" style="left:689px;border-top-style:solid">
    <div class="tile" style="background:#12125a">
      <svg width="44" height="44" viewBox="0 0 44 44" fill="none" stroke="#fff" stroke-width="1.6"><circle cx="22" cy="10" r="4"/><circle cx="12" cy="16" r="3"/><circle cx="32" cy="16" r="3"/><path d="M8 24l6 14h16l6-14"/><path d="M15 24c2-4 4-6 7-6s5 2 7 6"/></svg>
      2022: 4TH YEAR
    </div>
  </div>
  <svg class="abs" style="left:357px;top:232px" width="340" height="16" viewBox="0 0 340 16">
    <line x1="0" y1="8" x2="40" y2="8" stroke="#444" stroke-width="1.2"/><polygon points="46,8 38,4 38,12" fill="#444"/>
    <line x1="286" y1="8" x2="326" y2="8" stroke="#444" stroke-width="1.2"/><polygon points="332,8 324,4 324,12" fill="#444"/>
  </svg>
  <ul class="bullets recap-list" style="left:167px">
    <li>Premium: $686k</li><li>New Clients: 33.5</li><li>AUM: $5.3M</li><li>GDC growth: 455%</li>
    <li>2nd Marco Delgado at 403%</li><li>3rd was Ben Porter at 247%</li><li>4th Kaplan at 109%</li><li>West Ranking: #1</li>
  </ul>
  <ul class="bullets recap-list" style="left:418px">
    <li>Premium: $573k</li><li>New Clients: 56</li><li>Net New AUM: $5.4M</li><li>GDC growth: 242 %</li>
    <li>2nd closest was Owen Hale at 45%</li><li>West Ranking: #3</li>
  </ul>
  <ul class="bullets recap-list" style="left:742px">
    <li>Premium: $513K</li><li>New Clients: 45</li><li>Net New AUM: $5.9M</li><li>GDC growth: 77%</li>
    <li>2nd Owen Hale at 56%</li><li>3rd Kaplan at 53%</li><li>West Ranking: #2</li>
  </ul>
  <div class="footer-line"></div><div class="page-no"><span>5</span></div>
</section>

<!-- Slide 6: outside AUM -->
<section class="slide" style="top:3375px">
  <h2 class="title">OUTSIDE AUM</h2>
  <svg class="abs" style="left:0;top:0" width="1046" height="588" viewBox="0 0 1046 588">
    <circle cx="522" cy="307" r="115" fill="none" stroke="#fdbd08" stroke-width="2"/>
    <g fill="none" stroke="#fdbd08" stroke-width="1.5">
      <polyline points="354,225 380,225 422,254"/>
      <polyline points="354,400 380,400 422,362"/>
      <polyline points="690,225 664,225 622,254"/>
      <polyline points="690,400 664,400 622,362"/>
    </g>
    <g fill="#fff" stroke="#fdbd08" stroke-width="2">
      <circle cx="422" cy="254" r="4"/><circle cx="422" cy="362" r="4"/>
      <circle cx="622" cy="254" r="4"/><circle cx="622" cy="362" r="4"/>
    </g>
  </svg>
  <div class="photo" style="left:427px;top:212px;width:190px;height:190px;border-radius:50%;background:radial-gradient(circle at 50% 45%,#e6eaf0 0%,#a9b3c1 60%,#5d6676 100%)" role="img" aria-label="Photo of a team meeting around a table with laptops and charts"></div>
  <div class="aum-icon" style="left:284px;top:190px">
    <svg width="36" height="36" viewBox="0 0 36 36" fill="none" stroke="#fff" stroke-width="1.6"><circle cx="18" cy="14" r="9"/><path d="M15 11h5a2 2 0 0 1 0 4h-4a2 2 0 0 0 0 4h5M18 8v2M18 19v2"/><path d="M6 32c3-4 8-5 12-5s9 1 12 5"/></svg>
  </div>
  <div class="aum-icon" style="left:284px;top:365px">
    <svg width="36" height="36" viewBox="0 0 36 36" fill="none" stroke="#fff" stroke-width="1.6"><polyline points="5,26 13,18 19,22 30,10"/><polyline points="24,10 30,10 30,16"/><circle cx="12" cy="30" r="3"/><circle cx="24" cy="30" r="3"/></svg>
  </div>
  <div class="aum-icon" style="left:690px;top:190px">
    <svg width="36" height="36" viewBox="0 0 36 36" fill="none" stroke="#fff" stroke-width="1.6"><path d="M8 20c0-6 5-10 11-10s10 4 10 9c0 3-2 5-3 6v5h-4v-3h-6v3h-4v-5c-2-1-4-3-4-5z"/><circle cx="18" cy="6" r="3"/></svg>
  </div>
  <div class="aum-icon" style="left:690px;top:365px">
    <svg width="36" height="36" viewBox="0 0 36 36" fill="none" stroke="#fff" stroke-width="1.6"><rect x="5" y="7" width="26" height="18"/><line x1="18" y1="25" x2="18" y2="31"/><line x1="11" y1="31" x2="25" y2="31"/><line x1="10" y1="16" x2="26" y2="16"/><polyline points="21,12 26,16 21,20"/></svg>
  </div>
  <div class="aum-label" style="right:780px;top:204px;text-align:right">SHOW NUMBER FOR TOTAL<br>MOVEABLE OUTSIDE AUM</div>
  <div class="aum-label" style="right:780px;top:381px;text-align:right">ASSUME WE MOVE A<br>PERCENTAGE OF THAT 10%</div>
  <div class="aum-label" style="left:785px;top:215px">PLANNED SAVINGS</div>
  <div class="aum-label" style="left:785px;top:390px">MONTHLY EFT</div>
  <div class="footer-line"></div><div class="page-no"><span>6</span></div>
</section>

</body>
</html>
```